Lumo4Kart - a fintech company - business card

We need a business card design for our Payments Technology company in Sydney, Australia. We provide business with payment solutions expanding across EFTPOS machines, online payment gateways and mobile payment solutions. We would like to see designs that are clean, classy and professional.
Target Market(s)
Business professionals, executives, c-suite
Industry/Entity Type
Fintech
Contact Information for Business Card
Will be on 400gsm. Logo will most likely be spot gloss unless designer recommends otherwise.
Font styles to use
Sans Serif
Requirements
Must have
- We need our website (lumo4kart.com.au), email (contact@lumo4kart.com.au), mobile (0432 587 904) and direct phone number (02 6815 3927) to feature on the card along with our logo (attached) and the words "EFTPOS | ONLINE | MOBILE"
- Font = Roboto

```html
<!DOCTYPE html>
<html lang="en">
<head>
<meta charset="utf-8">
<title>Lumo4Kart business card</title>
<link rel="stylesheet" href="https://fonts.googleapis.com/css2?family=Roboto:wght@300;400;500;700&display=swap">
<style>
  :root {
    --backdrop: #b4b4b4;
    --card-white: #ffffff;
    --card-grey: #5e5f61;
    --card-grey-light: #6c6d70;
    --brand-blue: #23609c;
    --text-grey: #6b6d70;
    --text-dark: #4a4c4f;
    --faint-shape: #e7ebef;
  }
  * { margin: 0; padding: 0; box-sizing: border-box; }
  html, body {
    width: 1200px;
    height: 675px;
    overflow: hidden;
    background: var(--backdrop);
    font-family: "Roboto", Arial, sans-serif;
  }
  .stage {
    width: 1200px;
    height: 675px;
    display: flex;
    align-items: center;
    justify-content: center;
    gap: 60px;
  }
  .card {
    position: relative;
    width: 500px;
    height: 286px;
    border-radius: 18px;
    overflow: hidden;
    box-shadow: 0 10px 24px rgba(0,0,0,0.18);
  }
  /* Front */
  .card-front { background: var(--card-white); }
  .card-front .accent-shape {
    position: absolute;
    left: 0; top: 0;
    width: 500px; height: 286px;
  }
  .holder {
    position: absolute;
    left: 70px;
    top: 128px;
    width: 170px;
    text-align: right;
  }
  .holder-name {
    font-weight: 500;
    font-size: 18px;
    letter-spacing: 0.5px;
    color: var(--brand-blue);
    line-height: 1.1;
  }
  .holder-title {
    font-weight: 400;
    font-size: 13px;
    color: var(--text-grey);
    margin-top: 1px;
  }
  .contact-list {
    position: absolute;
    left: 262px;
    top: 92px;
    list-style: none;
  }
  .contact-list li {
    display: flex;
    align-items: center;
    gap: 10px;
    font-size: 13px;
    font-weight: 300;
    color: var(--text-grey);
    line-height: 1;
    height: 19px;
  }
  .contact-list svg {
    width: 12px;
    height: 12px;
    flex: none;
  }
  .services {
    position: absolute;
    left: 0; right: 0;
    bottom: 30px;
    text-align: center;
    font-size: 14px;
    font-weight: 500;
    letter-spacing: 1.4px;
    color: var(--text-dark);
  }
  /* Back */
  .card-back {
    background: linear-gradient(135deg, var(--card-grey-light) 0%, var(--card-grey) 55%, #58595b 100%);
  }
  .brand {
    position: absolute;
    inset: 0;
    display: flex;
    align-items: center;
    justify-content: center;
    gap: 16px;
  }
  .brand-dot {
    width: 46px;
    height: 46px;
    border-radius: 50%;
    background: var(--brand-blue);
  }
  .brand-name {
    font-weight: 700;
    font-size: 40px;
    letter-spacing: 1px;
    color: #ffffff;
  }
</style>
</head>
<body>
<main class="stage">
  <section class="card card-front" aria-label="Card front">
    <svg class="accent-shape" viewBox="0 0 500 286" aria-hidden="true">
      <circle cx="350" cy="40" r="120" fill="var(--faint-shape)"/>
    </svg>

    <div class="holder">
      <p class="holder-name">RAE CALLOWAY</p>
      <p class="holder-title">Manager</p>
    </div>

    <ul class="contact-list">
      <li>
        <svg viewBox="0 0 12 12" aria-hidden="true"><path d="M2.5 1 L4.5 1 L5.2 3.4 L4 4.4 C4.6 5.8 5.9 7.2 7.6 8 L8.6 6.8 L11 7.5 L11 9.5 C11 10.3 10.3 11 9.5 11 C5 11 1 7 1 2.5 C1 1.7 1.7 1 2.5 1 Z" fill="var(--brand-blue)"/></svg>
        02 6815 3927
      </li>
      <li>
        <svg viewBox="0 0 12 12" aria-hidden="true"><rect x="3" y="0.8" width="6" height="10.4" rx="1" fill="none" stroke="var(--brand-blue)" stroke-width="1.3"/><circle cx="6" cy="9.3" r="0.7" fill="var(--brand-blue)"/></svg>
        0432 587 904
      </li>
      <li>
        <svg viewBox="0 0 12 12" aria-hidden="true"><rect x="0.8" y="2.3" width="10.4" height="7.4" fill="none" stroke="var(--brand-blue)" stroke-width="1.3"/><path d="M1 2.6 L6 6.6 L11 2.6" fill="none" stroke="var(--brand-blue)" stroke-width="1.3"/></svg>
        contact@lumo4kart.com.au
      </li>
      <li>
        <svg viewBox="0 0 12 12" aria-hidden="true"><circle cx="6" cy="6" r="5" fill="none" stroke="var(--brand-blue)" stroke-width="1.2"/><ellipse cx="6" cy="6" rx="2.2" ry="5" fill="none" stroke="var(--brand-blue)" stroke-width="1"/><path d="M1 6 H11" stroke="var(--brand-blue)" stroke-width="1"/></svg>
        lumo4kart.com.au
      </li>
    </ul>

    <p class="services">EFTPOS | ONLINE | MOBILE</p>
  </section>

  <section class="card card-back" aria-label="Card back">
    <div class="brand">
      <span class="brand-dot" aria-hidden="true"></span>
      <span class="brand-name">LUMO4KART</span>
    </div>
  </section>
</main>
</body>
</html>
```